Location Map

Wanting a modern design of a map of Victoria Australia showing all of our office locations
i have attached associated company logos and map as refence

```html
<!DOCTYPE html>
<html lang="en">
<head>
<meta charset="utf-8">
<title>Office Locations – Victoria</title>
<link href="https://fonts.googleapis.com/css2?family=Poppins:wght@400;600&display=swap" rel="stylesheet">
<style>
  :root {
    --page: #ffffff;
    --land-top: #c3d8e0;
    --land-bottom: #e4eef2;
    --label: #3f3f3f;
    --footer: #d3d3d3;
    --pin-mildura: #c95cc9;
    --pin-swanhill: #5b8fcc;
    --pin-deniliquin: #2fb574;
    --pin-kp: #f28a1e;
    --pin-euroa: #5e0a06;
    --pin-setmour: #86ad25;
    --pin-portmelb: #14b0d0;
    --pin-bairnsdale: #ec2f24;
    --pin-sale: #0e5a78;
    --brand-teal: #0e8c7e;
    --brand-navy: #1d4f94;
    --brand-slate: #3a3f4a;
  }
  * { margin: 0; padding: 0; box-sizing: border-box; }
  html, body { width: 1200px; height: 1200px; overflow: hidden; background: var(--page); }
  .location-map {
    position: relative; width: 1200px; height: 1200px;
    font-family: "Poppins", sans-serif; background: var(--page);
  }
  .map-area {
    position: absolute; left: 0; top: 0; width: 1200px; height: 1055px;
    background: linear-gradient(180deg, var(--land-top) 0%, var(--land-bottom) 78%, var(--page) 100%);
  }
  .pin { position: absolute; width: 36px; height: 50px; }
  .pin svg { display: block; width: 36px; height: 50px; }
  .label {
    position: absolute; transform: translateY(-50%);
    font-weight: 600; font-size: 27px; line-height: 1; color: var(--label);
    letter-spacing: -0.3px; white-space: nowrap;
  }
  .label-stack { line-height: 34px; transform: none; }
  .partner-bar {
    position: absolute; left: 0; top: 1055px; width: 1200px; height: 145px;
    background: var(--footer);
    display: flex; align-items: center; justify-content: space-between;
    padding: 0 26px;
  }
  .partner { display: flex; align-items: center; gap: 10px; font-family: "Poppins", sans-serif; font-weight: 400; }
  .partner-mark { width: 46px; height: 46px; border-radius: 50%; }
  .partner-southbay { font-size: 38px; color: var(--brand-teal); }
  .partner-southbay .partner-mark { background: var(--brand-teal); }
  .partner-larkin { font-size: 15px; color: var(--brand-slate); line-height: 1.4; letter-spacing: 1.5px; text-transform: uppercase; }
  .partner-harbour { font-size: 20px; color: var(--brand-navy); line-height: 1.15; text-align: center; }
  .partner-keystone { font-size: 22px; color: var(--brand-slate); letter-spacing: 5px; line-height: 1.25; text-transform: uppercase; }
  .partner-keystone .partner-mark { width: 40px; height: 40px; border-radius: 0; background: var(--brand-slate); }
</style>
</head>
<body>
<svg width="0" height="0" style="position:absolute">
  <defs>
    <symbol id="map-pin" viewBox="0 0 36 50">
      <path d="M18 1C8.6 1 1 8.4 1 17.6c0 11.5 13.6 24.6 17 31.4 3.4-6.8 17-19.9 17-31.4C35 8.4 27.4 1 18 1z" fill="currentColor"/>
      <circle cx="18" cy="17" r="6.5" fill="#ffffff" opacity="0.85"/>
    </symbol>
  </defs>
</svg>

<main class="location-map">
  <div class="map-area" role="img" aria-label="Map of Victoria, Australia, with the southern coastline and Port Phillip Bay"></div>

  <div class="pin" style="left:120px;top:96px;color:var(--pin-mildura)"><svg><use href="#map-pin"/></svg></div>
  <div class="label" style="left:178px;top:115px">MILDURA</div>

  <div class="pin" style="left:323px;top:275px;color:var(--pin-swanhill)"><svg><use href="#map-pin"/></svg></div>
  <div class="label label-stack" style="left:372px;top:230px">LLIS<br>SWAN HILL<br>HLB<br>KP</div>

  <div class="pin" style="left:526px;top:310px;color:var(--pin-deniliquin)"><svg><use href="#map-pin"/></svg></div>
  <div class="label" style="left:573px;top:331px">DENILIQUIN</div>

  <div class="pin" style="left:490px;top:396px;color:var(--pin-kp)"><svg><use href="#map-pin"/></svg></div>
  <div class="label" style="left:539px;top:416px">KP</div>

  <div class="pin" style="left:616px;top:510px;color:var(--pin-euroa)"><svg><use href="#map-pin"/></svg></div>
  <div class="label" style="left:662px;top:530px">EUROA</div>

  <div class="pin" style="left:554px;top:561px;color:var(--pin-setmour)"><svg><use href="#map-pin"/></svg></div>
  <div class="label" style="left:599px;top:582px">SETMOUR</div>

  <div class="label" style="left:403px;top:652px">PORT MELBOURNE</div>
  <div class="pin" style="left:513px;top:678px;color:var(--pin-portmelb)"><svg><use href="#map-pin"/></svg></div>

  <div class="pin" style="left:881px;top:682px;color:var(--pin-bairnsdale)"><svg><use href="#map-pin"/></svg></div>
  <div class="label" style="left:924px;top:701px">BAIRNSDALE</div>

  <div class="pin" style="left:796px;top:737px;color:var(--pin-sale)"><svg><use href="#map-pin"/></svg></div>
  <div class="label" style="left:847px;top:763px">SALE</div>

  <footer class="partner-bar">
    <div class="partner partner-southbay"><span class="partner-mark"></span>Southbay Cover</div>
    <div class="partner partner-larkin">Larkin Lane<br>Insurance Services</div>
    <div class="partner partner-harbour">Harbour Lending<br>Brokers</div>
    <div class="partner partner-keystone"><span class="partner-mark"></span>Keystone<br>Planners</div>
  </footer>
</main>
</body>
</html>
```